New Property management company business cards

Looking for a new business card, to reflect new younger ownership
Card should be clean, simple and professional but with a modern layout that is conveys our new logo and business model

Key aspects of the business:

Property Management
Facility Maintenance
Project Management
Tenant Improvements

Mailing Address:
PO BOX 7186
Ridgeford CA, 95421

Phone: 209-614-8837
Direct: 209-614-8831

Doyle Farrant
President

Target Market(s)

Commercial property owners

Industry/Entity Type

Real Estate property management

Contact Information for Business Card

Open to all designs but lean toward vertical layouts

Requirements
Must have
• Logo and space to customize name and contact info

```html
<!DOCTYPE html>
<html lang="en">
<head>
<meta charset="utf-8">
<title>Halvern Property Management – Business Card</title>
<link rel="stylesheet" href="https://fonts.googleapis.com/css2?family=Montserrat:wght@400;500;700&display=swap">
<style>
  :root {
    --backdrop: #3b3b3b;
    --card: #1c1c1c;
    --teal: #1fb5b0;
    --white: #f2f2f2;
    --emboss: #0e0e0e;
    --emboss-light: #2a2a2a;
  }
  * { box-sizing: border-box; margin: 0; padding: 0; }
  html, body {
    width: 1200px; height: 801px; overflow: hidden;
    background: var(--backdrop);
    font-family: "Montserrat", sans-serif;
  }
  .sheet {
    width: 1200px; height: 801px;
    display: flex; align-items: center; justify-content: center; gap: 40px;
  }
  .card {
    width: 540px; height: 309px;
    background: var(--card);
    border-bottom: 3px solid var(--teal);
    position: relative;
    box-shadow: 0 14px 30px rgba(0,0,0,.35);
  }
  /* front */
  .card-front { display: flex; }
  .brand-panel {
    width: 335px; display: flex; align-items: center; justify-content: center;
    padding-top: 30px;
  }
  .divider { width: 1px; background: var(--teal); }
  .brand {
    display: flex; align-items: center; gap: 12px;
    color: var(--white); font-weight: 500;
  }
  .brand-mark { width: 16px; height: 16px; background: var(--white); }
  .brand-name { line-height: 1.2; }
  .brand-name .primary { display: block; font-size: 34px; letter-spacing: 5px; }
  .brand-name .secondary { display: block; font-size: 10.5px; letter-spacing: 4.2px; }
  .contact-panel {
    flex: 1; padding: 34px 0 0 18px; color: var(--white);
    font-size: 11.5px; line-height: 1.45;
  }
  .contact-name { color: var(--teal); font-weight: 700; font-size: 17px; text-transform: uppercase; line-height: 1.1; }
  .contact-title { margin-bottom: 14px; }
  .contact-address { margin-bottom: 14px; }
  .contact-list { list-style: none; }
  .contact-list li { display: flex; align-items: center; gap: 6px; }
  .contact-list svg { width: 10px; height: 10px; flex: none; fill: var(--teal); }
  /* back */
  .card-back { display: flex; align-items: center; justify-content: center; }
  .brand-emboss { color: var(--emboss); text-shadow: 0 1px 0 var(--emboss-light); }
  .brand-emboss .brand-mark { background: var(--emboss); box-shadow: 0 1px 0 var(--emboss-light); }
</style>
</head>
<body>
<main class="sheet">
  <section class="card card-front">
    <div class="brand-panel">
      <div class="brand">
        <span class="brand-mark"></span>
        <span class="brand-name"><span class="primary">HALVERN</span><span class="secondary">PROPERTY MANAGEMENT</span></span>
      </div>
    </div>
    <div class="divider"></div>
    <div class="contact-panel">
      <p class="contact-name">Doyle Farrant</p>
      <p class="contact-title">President</p>
      <p class="contact-address">PO BOX 7186<br>Ridgeford CA, 95421</p>
      <ul class="contact-list">
        <li><svg viewBox="0 0 10 10"><path d="M2 0.5 L3.6 2.8 2.7 3.8 Q3.6 5.8 6.2 7.3 L7.2 6.4 9.5 8 8.4 9.5 Q3.5 9.2 0.5 1.6Z"/></svg>209-614-8837</li>
        <li><svg viewBox="0 0 10 10"><path d="M2.5 0 H7.5 V10 H2.5Z M3.5 1 V8 H6.5 V1Z"/></svg>209-614-8831</li>
        <li><svg viewBox="0 0 10 10"><path d="M0 2 H10 V8 H0Z M0.8 2.6 5 5.6 9.2 2.6" stroke="#1c1c1c" stroke-width="0.8"/></svg>info@halvernproperty.com</li>
        <li><svg viewBox="0 0 10 10"><circle cx="5" cy="5" r="5"/></svg>www.halvernproperty.com</li>
      </ul>
    </div>
  </section>
  <section class="card card-back">
    <div class="brand brand-emboss">
      <span class="brand-mark"></span>
      <span class="brand-name"><span class="primary">HALVERN</span><span class="secondary">PROPERTY MANAGEMENT</span></span>
    </div>
  </section>
</main>
</body>
</html>
```